Design Project for Digital Recruitment Business

I am launching a new website in the Digital Marketing Recruitment space here in the UK.We are a start up so this very much phase 1 with our web offering.

Key points:

- I think it will be aproximately 5- 8 pages

- I am looking for wordpress(open on this)) design and coding/ development.

- It really is going to be a brochure site on the whole so don't expect any huge integration. I would like an RSS feed to publish our jobs on our site. I can get the code for that from my recruitment database partner Quillmark, all i will need is a blank page for that section?.Connect Up,chirpnet etc as well.

-I already have the logo.(See attached)which you guys delivered brilliantly on :-)

some reference sites I like the look of: http://www.tavernbright.co.uk http://www.plinthworks.com/ http://www.webmavens.co.uk/

The menu bar on these sites are good, the language is good.I want contemporary and professional.It needs to connect to the viewer.
WE are in the social media space so that needs to fit/blend eg connectup,PB.

SUGGESTED APPROACH
So I guess the best starting point would be to just submit a home page design so i can judge the styles I like best.Then the finalists of that round can submit another section of the website to see the consistency in terms of look and feel. I will then pick someone to work one on one with to complete the design and do the coding. That way no one gets to waste valuable time and energy :-)

Feel free to ping me questions
Updates

Project Deadline Extended
Reason: Hello All, I am going to extend by a few days. I have been inundated with work.However I Plan to look at all your designs this week end and respond to all your Queries. Thanks for your Patience.

Hi guys

here is a little more about us

We know that the career success of the candidates we place can have a great impact on the success of your business. We have built a network of talented industry professionals and an extensive knowledge of the market and its changing trends. We focus on career management,advice and consultancy.With over 30 years experience in our team we feel confident we can deliver. Our specialisms are Creative and Design,Digital Marketing,Editorial and Content,User Experience,and Technology related to building Websites.

In today's world of continually adapting,surviving and thriving we recognise that you rise and fall by the people you hire.That is why an expert  is required to help find those people in business critical roles. So if your online Marketing strategy is behind the times or your website traffic is poor for example we can help find people on a contract and permanent basis to bridge the gap in you marketing and E-commerce team. Online Talentry are specialists in these areas and offer a consultative approach to working with your business. If your business grows as a result of the people you recruited through us we could not be happier. Honest,straightforward,professional.

In terms of home page the Menu bar is 4-5 topics at most. 90% of the traffic to this website will be Candidates so Jobs will be the best content along with the 6 skill sets/categories and everything social after that.Very like Plinth website I mentioned in the Brief. A couple of you are on the right tracks.
Hope this helps for now. I feel confident I can pick from one of you.

Kind regards

Martin

Soory one other thing,

RE; Images

People are tricky to do on Recruitment websites as its very PC and they dont look real enough.Animations of people are better in my humble opinion...

open to ideas/options

Thanks

Target Market(s)

marketeers,designers,ecommerce folks.

Industry/Entity Type

Business

Requirements
Must have
• open at this stage but obviously the logo design colours must sync with the overall look and feel.PB,chirpnet,findr+ must be dominant

```html
<!DOCTYPE html>
<html lang="en">
<head>
<meta charset="utf-8">
<title>Online Talentry – Digital Recruitment</title>
<link rel="stylesheet" href="https://fonts.googleapis.com/css2?family=Roboto+Condensed:wght@400&family=Open+Sans:wght@400;600&family=Arimo:wght@400&display=swap">
<style>
:root{
  --orange:#ff5a1f;
  --purple:#3a1a8c;
  --ink:#3c3c3c;
  --muted:#8a8a8a;
  --link:#8a1a9c;
  --chirp:#3aaee6;
  --footer:#1c1c1c;
  --white:#ffffff;
}
*{margin:0;padding:0;box-sizing:border-box}
html,body{width:1200px;height:979px;overflow:hidden;background:var(--white)}
body{position:relative;font-family:"Arimo",Arial,sans-serif;color:var(--ink)}
.abs{position:absolute}

/* header */
.brand{left:141px;top:14px;display:flex;align-items:center;gap:10px;
  font-family:"Open Sans",sans-serif;font-weight:600;font-size:30px;color:var(--orange);letter-spacing:-0.5px}
.brand-mark{width:40px;height:40px;border-radius:50%;background:var(--orange)}
.nav{top:28px;left:577px;display:flex;align-items:center;font-family:"Roboto Condensed",sans-serif;font-size:15px}
.nav a{color:var(--purple);text-decoration:none;height:32px;line-height:32px;text-transform:uppercase}
.nav .active{background:var(--orange);color:var(--white);padding:0 17px;border-radius:3px;margin-right:28px}
.nav .item{margin-right:30px}
.social-top{left:987px;top:28px;display:flex;gap:9px}
.dot-icon{width:26px;height:26px;border-radius:50%}
.chirp{background:radial-gradient(circle at 35% 30%,#8fd8fb,var(--chirp))}

/* categories */
.cat{top:92px;width:150px;text-align:center}
.cat svg{display:block;margin:0 auto}
.cat-label{font-family:"Roboto Condensed",sans-serif;font-size:16px;color:#2a2a2a;margin-top:10px}

/* banner */
.banner{left:0;top:260px;width:1200px;height:399px;
  background:radial-gradient(ellipse at 70% 40%,#fafafa 0%,#ececec 55%,#dedede 100%)}
.banner-title{left:170px;top:372px;font-family:"Open Sans",sans-serif;font-weight:400;font-size:36px;color:var(--orange);letter-spacing:-1px}
.banner-sub{left:172px;top:427px;font-family:"Open Sans",sans-serif;font-size:14.5px;color:#444;white-space:pre}
.banner-art{left:553px;top:305px;width:424px;height:352px;
  background:radial-gradient(ellipse 50% 55% at 55% 50%,rgba(32,140,205,.85) 0%,rgba(58,178,225,.55) 45%,rgba(185,233,246,.25) 75%,rgba(236,236,236,0) 100%)}
.pager{left:143px;top:629px;display:flex;gap:6px}
.pager span{width:13px;height:13px;border-radius:50%;background:#9a9a9a;border:2px solid #f4f4f4;box-shadow:0 0 0 1px #bdbdbd}
.pager .on{background:var(--orange)}

/* panels */
.panel-head{top:683px;font-family:"Open Sans",sans-serif;font-weight:400;font-size:16.5px;color:var(--purple);display:flex;align-items:center;gap:8px}
.head-icon{width:19px;height:19px;border-radius:3px}
.panel{top:711px;width:283px;height:189px;background:var(--white);border:1px solid #dcdcdc;
  box-shadow:0 10px 8px -8px rgba(0,0,0,.35);padding:16px 14px 0 15px;font-size:13px}
.entry{margin-bottom:14px}
.entry-title{color:#555;line-height:16px}
.entry-meta{font-size:10.5px;color:var(--muted);margin-top:4px}
.entry-meta .author{color:var(--link)}
.view-all{position:absolute;right:18px;bottom:14px;font-size:11.5px;color:var(--link)}
.view-all::before{content:"→ ";font-size:9px;color:#555}

/* footer */
.footer{left:0;top:934px;width:1200px;height:45px;background:var(--footer)}
.footer-links{left:141px;top:952px;font-size:11.5px;color:#d8d8d8;word-spacing:1px}
.follow{left:907px;top:944px;display:flex;align-items:center;gap:14px;
  font-family:"Roboto Condensed",sans-serif;font-size:14px;color:#d8d8d8}
.follow .dot-icon{width:30px;height:30px}
</style>
</head>
<body>

<header>
  <div class="abs brand"><span class="brand-mark"></span>Online Talentry</div>
  <nav class="abs nav">
    <a class="active" href="#">Jobs</a>
    <a class="item" href="#">Resources</a>
    <a class="item" href="#">About us</a>
    <a class="item" href="#">Contact us</a>
  </nav>
  <div class="abs social-top">
    <span class="dot-icon chirp" aria-label="Chirpnet"></span>
    <svg class="dot-icon" viewBox="0 0 26 26" aria-label="RSS"><circle cx="13" cy="13" r="13" fill="#f07810"/><circle cx="8.5" cy="17.5" r="2" fill="#fff"/><path d="M7 11a8 8 0 0 1 8 8M7 6.5a12.5 12.5 0 0 1 12.5 12.5" stroke="#fff" stroke-width="2.2" fill="none"/></svg>
  </div>
</header>

<section class="categories">
  <div class="abs cat" style="left:133px">
    <svg width="128" height="128" viewBox="0 0 128 128"><circle cx="64" cy="64" r="63" fill="var(--orange)"/><circle cx="64" cy="64" r="57" fill="none" stroke="#b83a0a" stroke-width="1.2" stroke-dasharray="3 3"/><circle cx="64" cy="64" r="34" fill="#f3d2bd" role="img" aria-label="Illustration of a mug holding brushes and pencils"/></svg>
    <div class="cat-label">Creative and Design</div>
  </div>
  <div class="abs cat" style="left:291px">
    <svg width="128" height="128" viewBox="0 0 128 128"><circle cx="64" cy="64" r="63" fill="var(--orange)"/><circle cx="64" cy="64" r="57" fill="none" stroke="#b83a0a" stroke-width="1.2" stroke-dasharray="3 3"/><circle cx="64" cy="64" r="38" fill="#6b7fd0" role="img" aria-label="Illustration of a cluster of social network bubbles"/></svg>
    <div class="cat-label">Digital Marketing</div>
  </div>
  <div class="abs cat" style="left:448px">
    <svg width="128" height="128" viewBox="0 0 128 128"><circle cx="64" cy="64" r="63" fill="var(--orange)"/><circle cx="64" cy="64" r="57" fill="none" stroke="#b83a0a" stroke-width="1.2" stroke-dasharray="3 3"/><circle cx="64" cy="64" r="34" fill="#4a3a36" role="img" aria-label="Illustration of a figure writing with a giant pencil"/></svg>
    <div class="cat-label">Editorial and Content</div>
  </div>
  <div class="abs cat" style="left:607px">
    <svg width="128" height="128" viewBox="0 0 128 128"><circle cx="64" cy="64" r="63" fill="var(--orange)"/><circle cx="64" cy="64" r="57" fill="none" stroke="#b83a0a" stroke-width="1.2" stroke-dasharray="3 3"/><circle cx="64" cy="64" r="34" fill="#9aa4ad" role="img" aria-label="Illustration of a robot holding a globe"/></svg>
    <div class="cat-label" style="margin-top:8px">Technology</div>
  </div>
  <div class="abs cat" style="left:764px">
    <svg width="128" height="128" viewBox="0 0 128 128"><circle cx="64" cy="64" r="63" fill="var(--orange)"/><circle cx="64" cy="64" r="57" fill="none" stroke="#b83a0a" stroke-width="1.2" stroke-dasharray="3 3"/><circle cx="64" cy="64" r="34" fill="#e9c9a8" role="img" aria-label="Illustration of two users with an add sign"/></svg>
    <div class="cat-label">User Experience</div>
  </div>
  <div class="abs cat" style="left:922px">
    <svg width="128" height="128" viewBox="0 0 128 128"><circle cx="64" cy="64" r="63" fill="var(--orange)"/><circle cx="64" cy="64" r="57" fill="none" stroke="#b83a0a" stroke-width="1.2" stroke-dasharray="3 3"/><circle cx="64" cy="64" r="34" fill="#3f8fc6" role="img" aria-label="Illustration of a globe with a gear"/></svg>
    <div class="cat-label">Project Management</div>
  </div>
</section>

<section class="hero">
  <div class="abs banner"></div>
  <h1 class="abs banner-title">MY DREAM JOB</h1>
  <p class="abs banner-sub">Devlop   -   Skill   -   Educate   -   Career</p>
  <div class="abs banner-art" role="img" aria-label="Illustration of blue silhouettes of a group of business people"></div>
  <div class="abs pager"><span class="on"></span><span></span><span></span></div>
</section>

<section class="panels">
  <h2 class="abs panel-head" style="left:149px">Dream Jobs
    <svg class="head-icon" viewBox="0 0 19 19"><rect width="19" height="19" rx="3" fill="#f07810"/><circle cx="5" cy="14" r="1.8" fill="#fff"/><path d="M3.5 8.5a7 7 0 0 1 7 7M3.5 4a11.5 11.5 0 0 1 11.5 11.5" stroke="#fff" stroke-width="1.8" fill="none"/></svg>
  </h2>
  <div class="abs panel" style="left:148px">
    <div class="entry"><div class="entry-title">Financial Accountant &nbsp;| &nbsp;Business Analyst</div><div class="entry-meta">By autor name, &nbsp; Deadline : October 31</div></div>
    <div class="entry"><div class="entry-title">Financial Accountant &nbsp;| &nbsp;Business Analyst</div><div class="entry-meta">By autor name, &nbsp; Deadline : October 31</div></div>
    <div class="entry"><div class="entry-title">Financial Accountant &nbsp;| &nbsp;Business Analyst</div><div class="entry-meta">By autor name, &nbsp; Deadline : October 31</div></div>
    <a class="view-all">Viewl all jobs</a>
  </div>

  <h2 class="abs panel-head" style="left:460px">Dream Hire
    <svg class="head-icon" viewBox="0 0 19 19"><circle cx="9.5" cy="9.5" r="7.5" fill="none" stroke="#e0481a" stroke-width="2"/><path d="M6 9.5l2.5 2.5 5-5" stroke="#5aa02c" stroke-width="2" fill="none"/></svg>
  </h2>
  <div class="abs panel" style="left:459px">
    <div class="entry"><div class="entry-title">Brands need real friends not Likes' | News | Market Ledger</div><div class="entry-meta"><span class="author">By autor name</span>, 4hrs ago</div></div>
    <div class="entry" style="margin-top:20px"><div class="entry-title">Brands need real friends not Likes' | News | Market Ledger</div><div class="entry-meta"><span class="author">By autor name</span>, 4hrs ago</div></div>
    <a class="view-all">Viewl all jobs</a>
  </div>

  <h2 class="abs panel-head" style="left:770px">Chirpnet feed
    <span class="head-icon chirp"></span>
  </h2>
  <div class="abs panel" style="left:771px">
    <div class="entry"><div class="entry-title">Brands need real friends not Likes' | News | Market Ledger</div><div class="entry-meta"><span class="author">By autor name</span>, 4hrs ago</div></div>
    <div class="entry" style="margin-top:20px"><div class="entry-title">Brands need real friends not Likes' | News | Market Ledger</div><div class="entry-meta"><span class="author">By autor name</span>, 4hrs ago</div></div>
    <a class="view-all">Viewl all jobs</a>
  </div>
</section>

<footer>
  <div class="abs footer"></div>
  <p class="abs footer-links">©Copyright 2012 onlinetalentry. All rights reserved &nbsp;/ &nbsp; Privacy policy &nbsp; / &nbsp; Terms and conditions</p>
  <div class="abs follow">Follow us on
    <span class="dot-icon chirp"></span>
    <svg class="dot-icon" viewBox="0 0 26 26" aria-label="RSS"><circle cx="13" cy="13" r="13" fill="#f07810"/><circle cx="8.5" cy="17.5" r="2" fill="#fff"/><path d="M7 11a8 8 0 0 1 8 8M7 6.5a12.5 12.5 0 0 1 12.5 12.5" stroke="#fff" stroke-width="2.2" fill="none"/></svg>
  </div>
</footer>

</body>
</html>
```